Black Leather Bound Gold Embossed Book Cover Art Wanted!

Need an art piece for my new book. The book will be wrapped in black leather and the art and title will be gold embossed. The art piece is to be placed in the centre of the cover. The art needs to creatively convey the messages within the book while maintaining a simple beauty and elegance to fit the overall feel of the book.

The book is not intended to make me money but is a passion project and a labour of love. I'm looking for an art piece that best expresses the ideas presented in the book.

Please check the uploaded files for a more in depth brief and a copy of the book (Don't worry, it's short!). If you gave any questions please do not hesitate to get in contact with me.
Updates

Low designer entries

After a review of the submissions I have decided I was not overly clear in what I was after. I have updated the brief with an image that I have drawn that I would like the artists to use as a starting point and extrapolate from. Thank you everyone for their submissions so far.

Requirements
Must have
• Please see 'Book Art Brief' PDF attached
Nice to have
Should not have

```html
<!DOCTYPE html>
<html lang="en">
<head>
<meta charset="utf-8">
<title>Conversations — Book Cover</title>
<link rel="stylesheet" href="https://fonts.googleapis.com/css2?family=Tinos&display=swap">
<style>
  :root {
    --backdrop: #d9d9d9;
    --paper: #ffffff;
    --ink: #111111;
  }
  html, body {
    margin: 0;
    padding: 0;
    width: 1200px;
    height: 1200px;
    overflow: hidden;
    background: var(--backdrop);
  }
  .cover {
    position: absolute;
    left: 224px;
    top: 66px;
    width: 755px;
    height: 1068px;
    background: var(--paper);
    font-family: "Tinos", "Times New Roman", serif;
    color: var(--ink);
  }
  .flourish {
    position: absolute;
    left: 50%;
    transform: translateX(-50%);
    background: linear-gradient(to bottom, transparent 40%, var(--ink) 40%, var(--ink) 60%, transparent 60%);
    border-radius: 4px;
  }
  .flourish--crown { top: 88px; width: 290px; height: 36px; }
  .flourish--under-title { top: 272px; width: 240px; height: 24px; }
  .flourish--author { top: 958px; width: 118px; height: 16px; }
  .title {
    position: absolute;
    top: 146px;
    left: 0;
    right: 0;
    margin: 0;
    text-align: center;
    font-size: 75px;
    font-weight: 400;
    line-height: 1;
  }
  .tagline {
    position: absolute;
    top: 220px;
    left: 0;
    right: 0;
    margin: 0;
    text-align: center;
    font-size: 29px;
    line-height: 1;
  }
  .emblem {
    position: absolute;
    left: 152px;
    top: 366px;
    width: 448px;
    height: 460px;
    border-radius: 50%;
    box-sizing: border-box;
    border: 5px solid var(--ink);
    background: linear-gradient(120deg, var(--ink) 0%, var(--ink) 38%, #8a8a8a 50%, var(--paper) 64%, var(--paper) 100%);
  }
  .author {
    position: absolute;
    top: 922px;
    left: 0;
    right: 0;
    margin: 0;
    text-align: center;
    font-size: 26px;
    letter-spacing: 0.55em;
    padding-left: 0.55em;
    line-height: 1;
  }
</style>
</head>
<body>
  <main class="cover">
    <div class="flourish flourish--crown" role="img" aria-label="Ornamental scrollwork divider"></div>
    <h1 class="title">CONVERSATIONS</h1>
    <p class="tagline">headline or line from the book</p>
    <div class="flourish flourish--under-title" role="img" aria-label="Ornamental scrollwork divider"></div>
    <div class="emblem" role="img" aria-label="Central cover artwork: a circular black and white emblem of two stylised figures curled around each other like yin and yang, one dark and one light, facing each other in conversation"></div>
    <p class="author">AUTHOR NAME</p>
    <div class="flourish flourish--author" role="img" aria-label="Small ornamental scrollwork divider"></div>
  </main>
</body>
</html>
```